New Business Card

Would like a shiny card with Metallic logo raised on th front. Address 518 Whitlock Avenue, Toronto Ontario M4K2J8, phone 416 555 0182, email kvbe@lindenmail.ca and web www.kvbe.ca on the back in right and left lower corners balanced. Top of back should say Personalized Care for Pet's and their People centered. Leaving space on the back to write. Horizontal placement

Industry/Entity Type

Business

```html
<!DOCTYPE html>
<html lang="en">
<head>
<meta charset="utf-8">
<title>Kingsvale Animal Hospital – Business Card</title>
<link href="https://fonts.googleapis.com/css2?family=Exo+2:wght@500;600&family=Montserrat:wght@400;500&display=swap" rel="stylesheet">
<style>
  :root {
    --backdrop: #3a3a3c;
    --card-black: #1c1c1e;
    --card-edge: #2a2a2c;
    --metal: #d4d4d6;
    --paper: #ffffff;
    --write-line: #e2e2e4;
    --ink-light: #f2f2f2;
  }
  * { margin: 0; padding: 0; box-sizing: border-box; }
  html, body { width: 801px; height: 1200px; overflow: hidden; }
  body {
    background: var(--backdrop);
    position: relative;
    font-family: "Montserrat", sans-serif;
  }
  .card {
    position: absolute;
    left: 80px;
    width: 640px;
    height: 366px;
    border-radius: 26px;
    overflow: hidden;
    background: var(--card-black);
    box-shadow: 0 18px 40px rgba(0,0,0,0.45);
  }
  .card--front { top: 117px; }
  .card--back { top: 717px; }

  /* Front */
  .brand {
    position: absolute;
    inset: 0;
    display: flex;
    flex-direction: column;
    align-items: center;
    justify-content: center;
    gap: 12px;
    font-family: "Exo 2", sans-serif;
    font-weight: 600;
    color: var(--metal);
    text-transform: uppercase;
  }
  .brand__dot {
    width: 64px; height: 64px;
    border-radius: 50%;
    background: var(--metal);
    margin-bottom: 10px;
  }
  .brand__name { font-size: 52px; letter-spacing: 3px; line-height: 1; }
  .brand__sub { font-size: 18px; letter-spacing: 4px; line-height: 1; }

  /* Back */
  .tagline {
    position: absolute;
    top: 22px; left: 0; right: 0;
    text-align: center;
    font-family: "Exo 2", sans-serif;
    font-weight: 500;
    font-size: 26px;
    line-height: 1.15;
    letter-spacing: 1px;
    color: var(--ink-light);
    text-transform: uppercase;
  }
  .note-area {
    position: absolute;
    top: 100px; left: 0; right: 0;
    height: 150px;
    background: var(--paper);
    padding: 22px 40px 0;
  }
  .note-area__line {
    height: 1px;
    background: var(--write-line);
    margin-bottom: 30px;
  }
  .contact {
    position: absolute;
    left: 34px; bottom: 26px;
    list-style: none;
    color: var(--ink-light);
    font-size: 15px;
    line-height: 26px;
  }
  .contact__item { display: flex; align-items: center; gap: 10px; }
  .contact__icon { width: 14px; height: 14px; flex: none; }
  .address {
    position: absolute;
    right: 34px; bottom: 26px;
    text-align: right;
    color: var(--ink-light);
    font-size: 16px;
    line-height: 24px;
    font-style: normal;
  }
</style>
</head>
<body>

<section class="card card--front" aria-label="Card front">
  <div class="brand">
    <span class="brand__dot"></span>
    <span class="brand__name">Kingsvale</span>
    <span class="brand__sub">Animal Hospital</span>
  </div>
</section>

<section class="card card--back" aria-label="Card back">
  <h1 class="tagline">Personalized care for pet's<br>and their people</h1>

  <div class="note-area" aria-label="Space to write">
    <div class="note-area__line"></div>
    <div class="note-area__line"></div>
    <div class="note-area__line"></div>
    <div class="note-area__line"></div>
  </div>

  <ul class="contact">
    <li class="contact__item">
      <svg class="contact__icon" viewBox="0 0 16 16" aria-hidden="true"><circle cx="8" cy="8" r="7.2" fill="none" stroke="#f2f2f2" stroke-width="1"/><path d="M5.4 4.4l1.3 0 .6 1.7-.8.6a5 5 0 0 0 2.2 2.2l.6-.8 1.7.6v1.3c0 .4-.4.7-.8.7A6 6 0 0 1 4.7 5.2c0-.4.3-.8.7-.8z" fill="#f2f2f2"/></svg>
      416 555 0182
    </li>
    <li class="contact__item">
      <svg class="contact__icon" viewBox="0 0 16 16" aria-hidden="true"><circle cx="8" cy="8" r="7.2" fill="none" stroke="#f2f2f2" stroke-width="1"/><rect x="4.3" y="5.4" width="7.4" height="5.2" fill="none" stroke="#f2f2f2" stroke-width="1"/><path d="M4.3 5.6L8 8.5l3.7-2.9" fill="none" stroke="#f2f2f2" stroke-width="1"/></svg>
      kvbe@lindenmail.ca
    </li>
    <li class="contact__item">
      <svg class="contact__icon" viewBox="0 0 16 16" aria-hidden="true"><circle cx="8" cy="8" r="7.2" fill="none" stroke="#f2f2f2" stroke-width="1"/><circle cx="8" cy="8" r="3.6" fill="none" stroke="#f2f2f2" stroke-width="1"/><path d="M4.4 8h7.2M8 4.4c-1.4 1.8-1.4 5.4 0 7.2M8 4.4c1.4 1.8 1.4 5.4 0 7.2" fill="none" stroke="#f2f2f2" stroke-width=".8"/></svg>
      www.kvbe.ca
    </li>
  </ul>

  <address class="address">
    518 Whitlock Avenue<br>
    Toronto Ontario<br>
    M4K2J8
  </address>
</section>

</body>
</html>
```